Flyer Design

We are a new dental centre opening i would like to do a letter drop advising of our services, hours and location.

In addition to the flyer i would like to create a package for business cards, letter head and also magnets. With our colour theme being as in our logo.

Target Market(s)

Familys and adult females

Industry/Entity Type

Dental

```html
<!DOCTYPE html>
<html lang="en">
<head>
<meta charset="UTF-8">
<title>Lumen Dental Centre – Letterhead</title>
<link rel="stylesheet" href="https://fonts.googleapis.com/css2?family=Oswald:wght@300;400;600&display=swap">
<style>
  :root {
    --teal: #4cc3c3;
    --magenta: #b01e8e;
    --mist: #e3f1f4;
    --watermark: #f1f8f9;
    --ink: #3a3a3a;
    --paper: #ffffff;
  }
  * { margin: 0; padding: 0; box-sizing: border-box; }
  html, body { width: 848px; height: 1200px; overflow: hidden; background: var(--paper); }
  .letterhead {
    position: relative;
    width: 848px;
    height: 1200px;
    background: var(--paper);
    font-family: "Oswald", "Arial Narrow", sans-serif;
    overflow: hidden;
  }
  .brand-tab {
    position: absolute;
    left: 0;
    top: 0;
    width: 440px;
    height: 190px;
  }
  .brand-name {
    position: absolute;
    left: 92px;
    top: 48px;
    width: 280px;
    display: flex;
    align-items: center;
    gap: 12px;
    color: var(--teal);
    font-weight: 400;
    font-size: 40px;
    line-height: 1;
    letter-spacing: 0.5px;
  }
  .brand-dot {
    width: 18px;
    height: 18px;
    border-radius: 50%;
    background: var(--teal);
    flex: none;
  }
  .contact-block {
    position: absolute;
    left: 566px;
    top: 30px;
  }
  .centre-name {
    color: var(--magenta);
    font-weight: 600;
    font-size: 28px;
    line-height: 1.2;
    margin-left: 32px;
    margin-bottom: 8px;
  }
  .contact-list { list-style: none; }
  .contact-item {
    display: flex;
    align-items: center;
    gap: 14px;
    height: 27.5px;
    color: var(--ink);
    font-weight: 300;
    font-size: 15px;
  }
  .contact-icon { width: 18px; height: 18px; flex: none; }
  .background-mark {
    position: absolute;
    left: 64px;
    top: 600px;
    width: 720px;
    text-align: center;
    color: var(--watermark);
    font-weight: 400;
    font-size: 150px;
    line-height: 1;
  }
  .footer-band {
    position: absolute;
    left: 71px;
    top: 1178px;
    width: 706px;
    height: 22px;
    background: var(--magenta);
  }
</style>
</head>
<body>
<main class="letterhead">
  <svg class="brand-tab" viewBox="0 0 440 190" aria-hidden="true">
    <defs>
      <filter id="tab-shadow" x="-10%" y="-10%" width="120%" height="140%">
        <feDropShadow dx="0" dy="8" stdDeviation="6" flood-color="#000" flood-opacity="0.28"/>
      </filter>
    </defs>
    <path d="M40 0 H420 C425 95 330 170 230 172 C130 174 35 110 40 0 Z" fill="var(--mist)" filter="url(#tab-shadow)"/>
  </svg>

  <div class="brand-name"><span class="brand-dot"></span>Lumen Dental</div>

  <header class="contact-block">
    <h1 class="centre-name">Lumen Dental Centre</h1>
    <ul class="contact-list">
      <li class="contact-item">
        <svg class="contact-icon" viewBox="0 0 18 18" aria-hidden="true">
          <circle cx="9" cy="9" r="7" fill="none" stroke="var(--teal)" stroke-width="1.8"/>
          <ellipse cx="9" cy="9" rx="3" ry="7" fill="none" stroke="var(--teal)" stroke-width="1.4"/>
          <line x1="2" y1="9" x2="16" y2="9" stroke="var(--teal)" stroke-width="1.4"/>
        </svg>
        27 Harbour View Rd, Brookvale
      </li>
      <li class="contact-item">
        <svg class="contact-icon" viewBox="0 0 18 18" aria-hidden="true">
          <path d="M5 2 L7.5 5.5 L6 7.5 C7 10 8.5 11.5 10.5 12.5 L12.5 11 L16 13.5 L14.5 16 C9 16 2 9 2.5 3.5 Z" fill="var(--teal)"/>
        </svg>
        9000 4821
      </li>
      <li class="contact-item">
        <svg class="contact-icon" viewBox="0 0 18 18" aria-hidden="true">
          <circle cx="9" cy="9" r="7.5" fill="var(--teal)"/>
          <circle cx="9" cy="9" r="2.5" fill="none" stroke="#fff" stroke-width="1.4"/>
          <path d="M11.5 7 V10.5 C11.5 12 13.5 12 13.5 10 A4.5 4.5 0 1 0 11.5 12.8" fill="none" stroke="#fff" stroke-width="1.2"/>
        </svg>
        hello@lumendental.com
      </li>
      <li class="contact-item">
        <svg class="contact-icon" viewBox="0 0 18 18" aria-hidden="true">
          <rect x="1.5" y="4" width="15" height="10" rx="1.5" fill="var(--teal)"/>
        </svg>
        www.lumendental.com
      </li>
    </ul>
  </header>

  <div class="background-mark" aria-hidden="true">Lumen Dental</div>

  <div class="footer-band"></div>
</main>
</body>
</html>
```